Re-Design the flow of the Keystride Principles

The keystride principle is a 10 step model that helps teams/organizations become high performing. Attached the model which i created. I love the design as it is but i used a template i don't owe the rights of so i would like to use this platform to see what you can come up with the redesign this flow while keeping the key elements in place. I like the flow, i like the cleanness and i like it to be compact.

Target Market(s)

Organizational change / Leadership/ Consultancy

Industry/Entity Type

Leadership

Requirements
Must have
• Keep as much as possible the flow and feel of the attached
Nice to have
• -Maybe some twist in how the different parts connect (not a must)
Should not have
• Less or more steps than added in the attached file

```html
<!DOCTYPE html>
<html lang="en">
<head>
<meta charset="utf-8">
<title>The Keystride Principles</title>
<link href="https://fonts.googleapis.com/css2?family=Arimo:wght@400;700&display=swap" rel="stylesheet">
<style>
  :root {
    --page: #ffffff;
    --panel: #656565;
    --panel-edge: #2e2e2e;
    --title: #f4f4f4;
    --accent: #3fa0ea;
    --bubble: #ffffff;
    --bubble-edge: #141414;
    --label-blue: #1f4f9e;
    --label-rose: #c8305c;
    --label-orange: #e0641c;
    --label-gold: #e2b826;
    --seg-green: #6cc21a;
    --seg-lavender: #9e9ef5;
    --seg-sky: #6a8df0;
    --seg-indigo: #5b5bef;
    --seg-royal: #0a3596;
    --seg-navy: #0d1b6e;
    --seg-plum: #5a1a8a;
    --seg-violet: #8a2bd0;
    --seg-magenta: #d91fd9;
    --seg-orange: #ff6a10;
    --seg-pink: #f79ccc;
  }
  * { margin: 0; padding: 0; box-sizing: border-box; }
  html, body { width: 1200px; height: 1000px; overflow: hidden; background: var(--page); }
  .canvas { position: relative; width: 1200px; height: 1000px; font-family: "Arimo", Arial, sans-serif; }
  .panel {
    position: absolute; left: 77px; top: 138px; width: 1046px; height: 724px;
    background: var(--panel); border: 1px solid var(--panel-edge);
  }
  .title {
    position: absolute; left: 0; right: 0; top: 200px; text-align: center;
    font-size: 58px; font-weight: 400; color: var(--title); letter-spacing: 0.3px; line-height: 1;
  }
  .title .accent { color: var(--accent); }
  .subtitle {
    position: absolute; left: 0; right: 0; top: 262px; text-align: center;
    font-size: 19.5px; color: var(--title); letter-spacing: 0.2px;
  }
  .flow { position: absolute; left: 0; top: 0; width: 1200px; height: 1000px; }
  .bubble { fill: var(--bubble); stroke: var(--bubble-edge); stroke-width: 1.2; }
  .pointer { fill: var(--bubble); }
  .label { font-family: "Arimo", Arial, sans-serif; font-size: 12.5px; }
  .label--blue { fill: var(--label-blue); font-weight: 700; }
  .label--rose { fill: var(--label-rose); }
  .label--orange { fill: var(--label-orange); }
  .label--gold { fill: var(--label-gold); }
  .icon { fill: none; stroke: #fff; stroke-width: 2; stroke-linecap: round; stroke-linejoin: round; }
  .icon-fill { fill: #fff; }
</style>
</head>
<body>
<div class="canvas">
  <div class="panel"></div>
  <h1 class="title">THE <span class="accent">KEYSTRIDE</span> PRINCIPLES</h1>
  <p class="subtitle">LIBERATE THE WORKPLACE &nbsp;UNLEASHING VALUE THROUGH PURPOSE AT EVERY LEVEL OF SCALE</p>

  <svg class="flow" viewBox="0 0 1200 1000" xmlns="http://www.w3.org/2000/svg">
    <g class="ring ring--right">
      <path fill="var(--seg-pink)" d="M752.7,451 A118,118 0 0 1 781.5,548.5 L736.1,541.3 A72,72 0 0 0 718.5,481.8 Z"/>
      <path fill="var(--seg-pink)" d="M667.1,412 A118,118 0 0 1 747,445.1 L715,478.2 A72,72 0 0 0 666.3,458 Z"/>
      <path fill="var(--seg-pink)" d="M581.6,446.6 A118,118 0 0 1 658.8,412.2 L661.2,458.1 A72,72 0 0 0 614.1,479.1 Z"/>
      <path fill="var(--seg-pink)" d="M547.3,521.8 A118,118 0 0 1 575.9,452.6 L610.7,482.8 A72,72 0 0 0 593.2,525 Z"/>
      <path fill="var(--seg-orange)" d="M780,556.5 A118,118 0 0 1 736,624.2 L708.3,587.5 A72,72 0 0 0 735.2,546.2 Z"/>
      <path fill="var(--seg-magenta)" d="M727.5,630.1 A118,118 0 0 1 648.6,646.9 L655,601.3 A72,72 0 0 0 703.2,591.1 Z"/>
      <path fill="var(--seg-violet)" d="M638.5,645 A118,118 0 0 1 573.3,604.3 L609,575.3 A72,72 0 0 0 648.8,600.2 Z"/>
      <path fill="var(--seg-plum)" d="M568.3,597.7 A118,118 0 0 1 547.1,534.1 L593,532.5 A72,72 0 0 0 606,571.3 Z"/>
    </g>
    <g class="ring ring--left">
      <path fill="var(--seg-green)" d="M463.8,647.8 A118,118 0 0 1 386.6,613.4 L419.1,580.9 A72,72 0 0 0 466.2,601.9 Z"/>
      <path fill="var(--seg-lavender)" d="M380.9,607.4 A118,118 0 0 1 352,530 L398,530 A72,72 0 0 0 415.7,577.2 Z"/>
      <path fill="var(--seg-sky)" d="M352.3,521.8 A118,118 0 0 1 386.6,446.6 L419.1,479.1 A72,72 0 0 0 398.2,525 Z"/>
      <path fill="var(--seg-indigo)" d="M392.6,440.9 A118,118 0 0 1 465.9,412.1 L467.5,458 A72,72 0 0 0 422.8,475.7 Z"/>
      <path fill="var(--seg-royal)" d="M474.1,412.1 A118,118 0 0 1 550.5,443.7 L519.1,477.3 A72,72 0 0 0 472.5,458 Z"/>
      <path fill="var(--seg-navy)" d="M556.3,449.5 A118,118 0 0 1 587.7,521.8 L541.8,525 A72,72 0 0 0 522.7,480.9 Z"/>
    </g>

    <g class="icons">
      <g transform="translate(431,617)"><path class="icon-fill" d="M0,11 L-12,-1 A6.5,6.5 0 0 1 0,-8 A6.5,6.5 0 0 1 12,-1 Z"/><path class="icon" stroke="var(--seg-green)" stroke-width="1.6" d="M-10,0 H-5 L-2,-5 L2,5 L4,0 H10"/></g>
      <g transform="translate(381,563)"><path class="icon" d="M-9,4 L7,-8 M-2,0 L-7,12 M-2,0 L3,12 M6,-10 L10,-4"/></g>
      <g transform="translate(383,491)"><circle class="icon" r="10"/><circle class="icon" r="4.5"/><path class="icon" d="M0,-14 V-6 M0,6 V14 M-14,0 H-6 M6,0 H14"/></g>
      <g transform="translate(435,442)" class="icon-fill"><circle cx="-9" cy="-9" r="3"/><circle cx="0" cy="-9" r="3"/><circle cx="9" cy="-9" r="3"/><rect x="-12" y="-4" width="6" height="13" rx="1.5"/><rect x="-3" y="-4" width="6" height="13" rx="1.5"/><rect x="6" y="-4" width="6" height="13" rx="1.5"/></g>
      <g transform="translate(506,442)"><path class="icon" d="M0,11 L-12,-1 A6.5,6.5 0 0 1 0,-8 A6.5,6.5 0 0 1 12,-1 Z"/><path class="icon" d="M-9,0 H-5 L-2,-5 L2,5 L4,0 H9"/></g>
      <g transform="translate(557,492)"><path class="icon" d="M-11,8 L-3,1 L2,5 L11,-5 M6,-5 H11 V0"/></g>
      <g transform="translate(575,560)"><circle class="icon" r="9"/><circle class="icon-fill" r="3.5"/></g>
      <g transform="translate(615,611)"><path class="icon" d="M0,-11 L0,11 M-11,0 L11,0 M-8,-8 L8,8 M8,-8 L-8,8"/></g>
      <g transform="translate(685,623)"><path class="icon" d="M-7,-9 H7 V-2 A7,7 0 0 1 -7,-2 Z M-7,-6 H-11 A4,4 0 0 0 -7,0 M7,-6 H11 A4,4 0 0 1 7,0 M0,5 V9 M-5,10 H5"/></g>
      <g transform="translate(745,582)"><circle class="icon" cx="-2" cy="-2" r="8"/><path class="icon" d="M4,4 L11,11 M-6,0 L-3,-4 L0,-1 L2,-5"/></g>
    </g>

    <g class="pointers">
      <path class="pointer" d="M418,412 L432,412 L424,420 Z"/>
      <path class="pointer" d="M515,405 L529,410 L519,418 Z"/>
      <path class="pointer" d="M640,402 L650,410 L634,414 Z"/>
      <path class="pointer" d="M347,482 L360,488 L347,494 Z"/>
      <path class="pointer" d="M346,572 L359,578 L346,584 Z"/>
      <path class="pointer" d="M418,648 L430,642 L426,654 Z"/>
      <path class="pointer" d="M538,566 L550,574 L538,580 Z"/>
      <path class="pointer" d="M602,652 L614,646 L610,658 Z"/>
      <path class="pointer" d="M684,654 L696,646 L696,660 Z"/>
      <path class="pointer" d="M792,580 L806,574 L806,588 Z"/>
    </g>

    <g class="step">
      <ellipse class="bubble" cx="393" cy="364" rx="64" ry="48" transform="rotate(-20 393 364)"/>
      <text class="label label--blue" transform="rotate(-22 395 364)" text-anchor="middle"><tspan x="395" y="341">Cultivate</tspan><tspan x="395" y="356">Psychological</tspan><tspan x="395" y="371">Safety and</tspan><tspan x="395" y="386">Ownership</tspan></text>
    </g>
    <g class="step">
      <ellipse class="bubble" cx="535" cy="356" rx="68" ry="48" transform="rotate(20 535 356)"/>
      <text class="label label--blue" transform="rotate(22 535 356)" text-anchor="middle"><tspan x="535" y="335">Tap into peoples</tspan><tspan x="535" y="350">Purpose and</tspan><tspan x="535" y="365">Passion (intrinsic</tspan><tspan x="535" y="380">motivation)</tspan></text>
    </g>
    <g class="step">
      <ellipse class="bubble" cx="692" cy="366" rx="66" ry="42" transform="rotate(12 692 366)"/>
      <text class="label label--blue" transform="rotate(12 692 366)" text-anchor="middle"><tspan x="692" y="354">Unlock culture of</tspan><tspan x="692" y="369">personal growth</tspan><tspan x="692" y="384">&amp; development</tspan></text>
    </g>
    <g class="step">
      <ellipse class="bubble" cx="303" cy="462" rx="45" ry="70" transform="rotate(15 303 462)"/>
      <text class="label label--blue" transform="rotate(-70 303 462)" text-anchor="middle"><tspan x="303" y="451">Develop a</tspan><tspan x="303" y="466">Master plan</tspan><tspan x="303" y="481">(strategy)</tspan></text>
    </g>
    <g class="step">
      <ellipse class="bubble" cx="301" cy="602" rx="48" ry="75"/>
      <text class="label label--blue"><tspan x="282" y="583">Identify</tspan><tspan x="282" y="598">Purpose</tspan><tspan x="282" y="613">Activators</tspan><tspan x="282" y="628">(Vision)</tspan></text>
    </g>
    <g class="step">
      <ellipse class="bubble" cx="403" cy="698" rx="73" ry="46" transform="rotate(20 403 698)"/>
      <text class="label label--blue"><tspan x="362" y="688">Discover your</tspan><tspan x="362" y="703">purpose. Why</tspan><tspan x="362" y="718">Do you exist?</tspan></text>
    </g>
    <g class="step">
      <ellipse class="bubble" cx="494" cy="598" rx="48" ry="72" transform="rotate(-20 494 598)"/>
      <text class="label label--blue"><tspan x="457" y="584">Prioritize</tspan><tspan x="457" y="599">Feedback &amp;</tspan><tspan x="457" y="614">Transparency</tspan></text>
    </g>
    <g class="step">
      <ellipse class="bubble" cx="595" cy="700" rx="72" ry="46" transform="rotate(20 595 700)"/>
      <text class="label label--rose"><tspan x="558" y="688">Empower the</tspan><tspan x="558" y="703">community from</tspan><tspan x="558" y="718">bottom</tspan></text>
    </g>
    <g class="step">
      <ellipse class="bubble" cx="737" cy="698" rx="72" ry="46" transform="rotate(-20 737 698)"/>
      <text class="label label--orange"><tspan x="686" y="690">Put excellent (team)</tspan><tspan x="686" y="705">performance in</tspan><tspan x="686" y="720">the spotlight</tspan></text>
    </g>
    <g class="step">
      <ellipse class="bubble" cx="850" cy="600" rx="48" ry="76" transform="rotate(12 850 600)"/>
      <text class="label label--gold"><tspan x="816" y="586">Monitor</tspan><tspan x="816" y="603">engagement</tspan><tspan x="816" y="620">Real</tspan></text>
    </g>
  </svg>
</div>
</body>
</html>
```